Game, Voice & Dedicated Server Company Needs a Business Card Design

We need a new business card design, centered around our new logo (PSD provided below).

Designs that we do like:
https://pixelmarsh.net/item/corporate-business-card/5382017?s_rank=43 (needs to be made more eye catching)

Our main areas of business are:
- Dedicated Servers
- Game Servers
- Voice Servers
- Mitigation Security Specialists

Industry/Entity Type

Business

Contact Information for Business Card

On the card: (and anything else you would suggest)
- Staff member name
- Staff member position in company
- Staff member phone number
- Staff member email
- Other / Staff member Skype
- Website link

Colors
9bcb3c
abd036

Requirements
Must have
• Design of Card:
• - Green (same green as the logo)
• - Business / Corporate design
• - Something a little different / abstract that shouts premium

```html
<!DOCTYPE html>
<html lang="en">
<head>
<meta charset="utf-8">
<title>Corvane Hosting – Business Card</title>
<link rel="stylesheet" href="https://fonts.googleapis.com/css2?family=Roboto:wght@400;700&display=swap">
<style>
  :root {
    --green: #9bcb3c;
    --green-deep: #8cc13a;
    --white: #ffffff;
    --stage: #3b3b3c;
    --stage-edge: #2e2e2f;
    --card-dark: #262627;
    --card-darker: #121212;
    --text-light: #f2f2f2;
    --text-muted: #e6e6e6;
  }
  * { box-sizing: border-box; margin: 0; padding: 0; }
  html, body {
    width: 999px; height: 1200px; overflow: hidden;
  }
  body {
    position: relative;
    background: radial-gradient(ellipse at center, var(--stage) 40%, var(--stage-edge) 100%);
    font-family: "Roboto", Arial, sans-serif;
  }

  .card { position: absolute; left: 34px; width: 931px; overflow: hidden; }

  /* Front */
  .card--front { top: 52px; height: 531px; }
  .front__top {
    position: absolute; left: 0; top: 0; width: 100%; height: 273px;
    background: var(--white);
  }
  .front__rule {
    position: absolute; left: 0; top: 273px; width: 100%; height: 9px;
    background: var(--green);
  }
  .front__bottom {
    position: absolute; left: 0; top: 282px; width: 100%; height: 249px;
    background: radial-gradient(ellipse 60% 90% at 72% 30%, #3a3a3b 0%, var(--card-dark) 45%, #1c1c1d 100%);
  }

  .brand { position: absolute; display: flex; align-items: center; }
  .brand__mark { background: var(--green); flex: none; }
  .brand__name {
    color: var(--green); font-weight: 700; text-transform: uppercase;
    line-height: 0.95; letter-spacing: -0.5px;
  }
  .brand--front { left: 226px; top: 86px; gap: 48px; }
  .brand--front .brand__mark { width: 110px; height: 110px; }
  .brand--front .brand__name { font-size: 50px; }

  .person { position: absolute; left: 49px; top: 427px; }
  .person__name { color: var(--green); font-weight: 700; font-size: 29px; }
  .person__role { color: var(--text-muted); font-size: 23px; margin-top: 10px; }

  .contacts { position: absolute; left: 543px; top: 311px; list-style: none; }
  .contacts__item {
    display: flex; align-items: center; height: 42px; margin-bottom: 10.5px;
    color: var(--text-light); font-size: 23px;
  }
  .contacts__icon {
    width: 42px; height: 42px; background: var(--green);
    display: flex; align-items: center; justify-content: center; margin-right: 12px;
  }
  .contacts__icon svg { width: 22px; height: 22px; }

  /* Back */
  .card--back {
    top: 605px; height: 532px;
    background: radial-gradient(ellipse 65% 70% at 50% 38%, #3a3a3b 0%, var(--card-dark) 45%, var(--card-darker) 100%);
  }
  .brand--back { left: 156px; top: 190px; gap: 54px; }
  .brand--back .brand__mark { width: 150px; height: 150px; }
  .brand--back .brand__name { font-size: 68px; }

  .back__band {
    position: absolute; left: 0; top: 435px; width: 100%; height: 43px;
    background: var(--green-deep);
    display: flex; align-items: center; justify-content: center;
    color: #1b1b1b; font-size: 25px; letter-spacing: 3.6px;
  }
</style>
</head>
<body>

  <section class="card card--front" aria-label="Business card front">
    <div class="front__top"></div>
    <div class="front__rule"></div>
    <div class="front__bottom"></div>

    <div class="brand brand--front">
      <span class="brand__mark"></span>
      <span class="brand__name">Corvane<br>Hosting</span>
    </div>

    <div class="person">
      <p class="person__name">Name Surname</p>
      <p class="person__role">CEO &amp; Managing Director</p>
    </div>

    <ul class="contacts">
      <li class="contacts__item">
        <span class="contacts__icon">
          <svg viewBox="0 0 24 24" fill="none" stroke="#fff" stroke-width="2.2" stroke-linecap="round" stroke-linejoin="round">
            <path d="M5 3h4l2 5-2.5 1.5a11 11 0 0 0 6 6L16 13l5 2v4a2 2 0 0 1-2 2A16 16 0 0 1 3 5a2 2 0 0 1 2-2z"/>
          </svg>
        </span>00 0000 0000
      </li>
      <li class="contacts__item">
        <span class="contacts__icon">
          <svg viewBox="0 0 24 24" fill="none" stroke="#fff" stroke-width="2.2" stroke-linecap="round">
            <rect x="6" y="2.5" width="12" height="19" rx="2"/>
            <line x1="10" y1="18" x2="14" y2="18"/>
          </svg>
        </span>0000 000 000
      </li>
      <li class="contacts__item">
        <span class="contacts__icon">
          <svg viewBox="0 0 24 24" fill="none" stroke="#fff" stroke-width="2.2" stroke-linejoin="round">
            <rect x="3" y="6" width="18" height="13" rx="1.5"/>
            <path d="M3 7l9 7 9-7"/>
          </svg>
        </span>info@corvane.com.au
      </li>
      <li class="contacts__item">
        <span class="contacts__icon">
          <svg viewBox="0 0 24 24" fill="none" stroke="#fff" stroke-width="1.8">
            <circle cx="12" cy="12" r="9"/>
            <ellipse cx="12" cy="12" rx="4" ry="9"/>
            <line x1="3" y1="12" x2="21" y2="12"/>
            <path d="M5 7h14M5 17h14"/>
          </svg>
        </span>www.corvane.com.au
      </li>
    </ul>
  </section>

  <section class="card card--back" aria-label="Business card back">
    <div class="brand brand--back">
      <span class="brand__mark"></span>
      <span class="brand__name">Corvane<br>Hosting</span>
    </div>
    <div class="back__band">www.corvane.com.au</div>
  </section>

</body>
</html>
```